Documentary Movie Needs a Poster

We need a poster/lobby card for a documentary film made by six filmmakers. Lobby card needs to list name of sponsor, names of filmmakers and (if feasible, but not required) image frames from each of the six sections of the film.

Text should be very readable. OK to have all caps text or upper/lower.

Design comps are OK, these do not need to be print-ready final images.

Target Market(s)

well educated documentary filmgoers

Industry/Entity Type

Movie

Requirements
Must have
• Must contain the following text (please use helvetica neue or similar font).

Please use the following sponsor name:

The
Marlowe Institute for Cinema
presents

Please use the following filmmaker names:

Theodore Pelusky
Robert Nash
Frederick Tamworth
Harold E. F. Pratt
Vincent Lorimer
Danny Frost

Please use the 6 images in archive/zip to create the card.

You can also do text-only versions of the card (no images).

Card needs to be 2:1 aspect ratio (2000px wide x 1000 pixels high)

Names of filmmakers should each be same size (no filmmaker has visual priority over the other).

Colors for text, lines and other design elements should be RED, BLACK and/or WHITE.

Feel free to crop images if you need to.

```html
<!DOCTYPE html>
<html lang="en">
<head>
<meta charset="utf-8">
<title>Marlowe Institute for Cinema presents</title>
<link href="https://fonts.googleapis.com/css2?family=Federo&family=Righteous&family=Special+Elite&display=swap" rel="stylesheet">
<style>
  :root {
    --side-blue: #5e9fcf;
    --side-blue-dark: #3f7fb4;
    --side-blue-light: #9cc7e6;
    --frame-red: #e0262b;
    --panel-edge: #c9601c;
    --panel-edge-light: #f08a3a;
    --panel-fill: #f3b552;
    --panel-fill-light: #f8cf7a;
    --title-red: #d8262a;
    --title-outline: #3a1208;
    --ink-brown: #3b2008;
    --presents-brown: #7a4a1c;
  }
  * { margin: 0; padding: 0; box-sizing: border-box; }
  html, body { width: 1200px; height: 600px; overflow: hidden; background: #ffffff; }
  .card {
    position: relative;
    width: 1200px;
    height: 600px;
    overflow: hidden;
    background:
      radial-gradient(circle at 20% 30%, var(--side-blue-light) 0 1px, transparent 2px) 0 0 / 7px 7px,
      radial-gradient(circle at 70% 60%, var(--side-blue-dark) 0 1px, transparent 2px) 0 0 / 5px 5px,
      var(--side-blue);
  }
  .card::before {
    content: "";
    position: absolute;
    inset: 0;
    box-shadow: inset 0 0 30px rgba(20, 60, 110, 0.55);
    pointer-events: none;
  }
  .frame {
    position: absolute;
    border: 3px solid var(--frame-red);
    border-radius: 14px;
    box-shadow: 2px 3px 6px rgba(0, 0, 0, 0.45);
  }
  .frame--l1 { left: 30px; top: 14px; width: 278px; height: 160px; transform: rotate(2deg);
    background: linear-gradient(180deg, #d9dde0 0%, #bfc3c4 45%, #8e8b86 70%, #a09a90 100%); }
  .frame--l2 { left: 24px; top: 196px; width: 282px; height: 196px; transform: rotate(-3deg);
    background: linear-gradient(180deg, #c9d2d8 0%, #a4a9a8 35%, #b59a78 65%, #6c5a44 100%); }
  .frame--l3 { left: 30px; top: 402px; width: 278px; height: 180px; transform: rotate(2deg);
    background: linear-gradient(180deg, #e6e9ec 0%, #b39a80 40%, #6b5a47 75%, #3f3a34 100%); }
  .frame--r1 { left: 892px; top: 8px; width: 280px; height: 192px; transform: rotate(2deg);
    background: linear-gradient(180deg, #dfe4e8 0%, #c8bfae 45%, #a99c84 75%, #d4c6a8 100%); }
  .frame--r2 { left: 890px; top: 205px; width: 280px; height: 180px; transform: rotate(2deg);
    background: linear-gradient(180deg, #eeeeee 0%, #b8b8b8 40%, #707070 75%, #3a3a3a 100%); }
  .frame--r3 { left: 890px; top: 398px; width: 276px; height: 186px; transform: rotate(-2deg);
    background: linear-gradient(180deg, #7fb2e6 0%, #a9c8e8 40%, #8f8a86 70%, #3d3a3a 100%); }

  .feature-panel {
    position: absolute;
    left: 330px;
    top: 0;
    width: 544px;
    height: 600px;
    border-radius: 10px;
    background: linear-gradient(90deg, var(--panel-edge) 0%, var(--panel-edge-light) 50%, var(--panel-edge) 100%);
    box-shadow: 0 0 10px rgba(0, 0, 0, 0.5);
  }
  .feature-panel__inner {
    position: absolute;
    inset: 16px;
    border-radius: 4px;
    background: radial-gradient(ellipse at 50% 40%, var(--panel-fill-light) 0%, var(--panel-fill) 70%, #e7a240 100%);
    box-shadow: inset 0 0 10px rgba(120, 50, 0, 0.45);
    text-align: center;
  }
  .sponsor {
    font-family: "Federo", sans-serif;
    font-weight: 400;
    color: var(--title-red);
    -webkit-text-stroke: 1.5px var(--title-outline);
    text-transform: uppercase;
    font-size: 50px;
    line-height: 56px;
    margin-top: 2px;
    text-shadow: 1px 2px 2px rgba(60, 20, 0, 0.35);
  }
  .sponsor__line { display: block; white-space: nowrap; }
  .presents {
    font-family: "Special Elite", monospace;
    color: var(--presents-brown);
    font-size: 34px;
    line-height: 40px;
    margin-top: 14px;
    margin-bottom: 16px;
  }
  .filmmakers { list-style: none; }
  .filmmakers li {
    font-family: "Righteous", sans-serif;
    color: var(--ink-brown);
    text-transform: uppercase;
    font-size: 36px;
    line-height: 51px;
    letter-spacing: 1px;
    white-space: nowrap;
  }
</style>
</head>
<body>
<main class="card">
  <div class="frame frame--l1" role="img" aria-label="Photo: soldier kneeling on a roadside during a patrol"></div>
  <div class="frame frame--l2" role="img" aria-label="Photo: soldiers on a rooftop overlooking a smoking city skyline"></div>
  <div class="frame frame--l3" role="img" aria-label="Photo: crowd of armed fighters raising rifles"></div>
  <div class="frame frame--r1" role="img" aria-label="Photo: wrecked armoured vehicle in the desert sand"></div>
  <div class="frame frame--r2" role="img" aria-label="Photo: black and white image of a soldier resting among rubble"></div>
  <div class="frame frame--r3" role="img" aria-label="Photo: anti-war protesters with signs in front of a capitol dome"></div>

  <section class="feature-panel">
    <div class="feature-panel__inner">
      <h1 class="sponsor">
        <span class="sponsor__line">The</span>
        <span class="sponsor__line">Marlowe Institute</span>
        <span class="sponsor__line">for Cinema</span>
      </h1>
      <p class="presents">presents</p>
      <ul class="filmmakers">
        <li>Theodore Pelusky</li>
        <li>Robert Nash</li>
        <li>Frederick Tamworth</li>
        <li>Harold E. F. Pratt</li>
        <li>Vincent Lorimer</li>
        <li>Danny Frost</li>
      </ul>
    </div>
  </section>
</main>
</body>
</html>
```